Design a Brazilian children's Bible calendar for 2017

We need someone to design a children's calendar for 2017 with an animal theme.
The format is 21cm x 15cm and we need the front cover and one page with two months as can be seen in the attached files.
Target Market(s)
Brazilian children
Font styles to use
Sans Serif
Requirements
Must have
- Modern, clean design

```html
<!DOCTYPE html>
<html lang="pt-BR">
<head>
<meta charset="utf-8">
<title>Calendário Infantil 2017 – Janeiro e Fevereiro</title>
<link rel="stylesheet" href="https://fonts.googleapis.com/css2?family=Fira+Sans:wght@500;600;700&display=swap">
<style>
  :root {
    --band-orange: #e9ae6b;
    --band-blue: #1492d6;
    --band-purple: #ddb2e6;
    --band-yellow: #fbe33c;
    --band-green: #bcda7d;
    --band-teal: #a0d0cc;
    --paper: #ffffff;
    --verse-yellow: #f7ec55;
    --frame-blue: #1c97d8;
    --weekday-blue: #1c97d8;
    --sunday-red: #c8203a;
    --number-ink: #231f20;
    --column-tint: #dcedf9;
    --jan-orange: #dd7f2b;
    --feb-green: #6cb573;
    --puppy-cream: #f4ebd6;
    --puppy-shadow: #e4cfae;
  }
  * { margin: 0; padding: 0; box-sizing: border-box; }
  html, body { width: 857px; height: 1200px; overflow: hidden; }
  body { font-family: "Fira Sans", "Open Sans", sans-serif; background: var(--paper); }

  .calendar-page { position: relative; width: 857px; height: 1200px; overflow: hidden; background: var(--paper); }

  .band { position: absolute; left: 0; width: 857px; }
  .band--orange { top: 0; height: 76px; background: var(--band-orange); }
  .band--blue { top: 86px; height: 356px; background: var(--band-blue); }
  .band--purple { top: 444px; height: 306px; background: var(--band-purple); }
  .band--yellow { top: 758px; height: 172px; background: var(--band-yellow); }
  .band--green { top: 936px; height: 186px; background: var(--band-green); }
  .band--teal { top: 1132px; height: 68px; background: var(--band-teal); }

  .verse { position: absolute; top: 116px; left: 0; width: 827px; text-align: center; color: var(--paper); }
  .verse__text { font-size: 46px; font-weight: 600; line-height: 56px; letter-spacing: 0.2px; }
  .verse__reference { margin-top: 16px; font-size: 24px; font-weight: 600; color: var(--verse-yellow); }

  .puppy-photo {
    position: absolute; left: 128px; top: 282px; width: 588px; height: 428px;
    border-radius: 46% 40% 30% 30% / 44% 48% 26% 26%;
    background: radial-gradient(ellipse at 55% 45%, var(--puppy-cream) 0%, #efe0c4 65%, var(--puppy-shadow) 100%);
  }

  .month {
    position: absolute; top: 787px; width: 380px; height: 306px;
    background: var(--paper); border: 2px solid var(--frame-blue); border-radius: 16px;
  }
  .month--january { left: 41px; }
  .month--february { left: 437px; }

  .month__title {
    position: absolute; left: 16px; top: 12px; width: 346px; height: 66px;
    border-radius: 16px 16px 44px 44px / 16px 16px 34px 34px;
    color: var(--paper); font-size: 37px; font-weight: 600;
    display: flex; align-items: center; justify-content: center;
  }
  .month--january .month__title { background: var(--jan-orange); }
  .month--february .month__title { background: var(--feb-green); }

  .month__grid {
    position: absolute; left: 16px; top: 80px;
    display: grid; grid-template-columns: repeat(7, 49.5px);
  }
  .month__column { display: flex; flex-direction: column; align-items: center; height: 212px; }
  .month__column--tinted { background: var(--column-tint); }

  .weekday { height: 34px; line-height: 34px; font-size: 16px; font-weight: 600; color: var(--weekday-blue); }
  .weekday--sunday { color: var(--sunday-red); }

  .day { height: 36px; line-height: 36px; font-size: 23px; font-weight: 700; color: var(--number-ink); }
  .month__column--sunday .day { color: var(--sunday-red); }
  .month__column--wednesday .day { transform: translateY(-4px); }
</style>
</head>
<body>
<main class="calendar-page">
  <div class="band band--orange"></div>
  <div class="band band--blue"></div>
  <div class="band band--purple"></div>
  <div class="band band--yellow"></div>
  <div class="band band--green"></div>
  <div class="band band--teal"></div>

  <header class="verse">
    <p class="verse__text">No princípio, criou Deus<br>os céus e a terra.</p>
    <p class="verse__reference">Gênesis 1 v 1</p>
  </header>

  <div class="puppy-photo" role="img" aria-label="Foto de dois filhotes de cachorro de pelo creme deitados juntos"></div>

  <section class="month month--january" aria-label="Janeiro 2017">
    <h2 class="month__title">Janeiro 2017</h2>
    <div class="month__grid">
      <div class="month__column month__column--sunday month__column--tinted"><span class="weekday weekday--sunday">Dom</span><span class="day">1</span><span class="day">8</span><span class="day">15</span><span class="day">22</span><span class="day">29</span></div>
      <div class="month__column"><span class="weekday">Seg</span><span class="day">2</span><span class="day">9</span><span class="day">16</span><span class="day">23</span><span class="day">30</span></div>
      <div class="month__column month__column--tinted"><span class="weekday">Ter</span><span class="day">3</span><span class="day">10</span><span class="day">17</span><span class="day">24</span><span class="day">31</span></div>
      <div class="month__column month__column--wednesday"><span class="weekday">Qua</span><span class="day">4</span><span class="day">11</span><span class="day">18</span><span class="day">25</span></div>
      <div class="month__column month__column--tinted"><span class="weekday">Qui</span><span class="day">5</span><span class="day">12</span><span class="day">19</span><span class="day">26</span></div>
      <div class="month__column"><span class="weekday">Sex</span><span class="day">6</span><span class="day">13</span><span class="day">20</span><span class="day">27</span></div>
      <div class="month__column month__column--tinted"><span class="weekday">Sáb</span><span class="day">7</span><span class="day">14</span><span class="day">21</span><span class="day">28</span></div>
    </div>
  </section>

  <section class="month month--february" aria-label="Fevereiro 2017">
    <h2 class="month__title">Fevereiro 2017</h2>
    <div class="month__grid">
      <div class="month__column month__column--sunday month__column--tinted"><span class="weekday weekday--sunday">Dom</span><span class="day"></span><span class="day">5</span><span class="day">12</span><span class="day">19</span><span class="day">26</span></div>
      <div class="month__column"><span class="weekday">Seg</span><span class="day"></span><span class="day">6</span><span class="day">13</span><span class="day">20</span><span class="day">27</span></div>
      <div class="month__column month__column--tinted"><span class="weekday">Ter</span><span class="day"></span><span class="day">7</span><span class="day">14</span><span class="day">21</span><span class="day">28</span></div>
      <div class="month__column month__column--wednesday"><span class="weekday">Qua</span><span class="day">1</span><span class="day">8</span><span class="day">15</span><span class="day">22</span></div>
      <div class="month__column month__column--tinted"><span class="weekday">Qui</span><span class="day">2</span><span class="day">9</span><span class="day">16</span><span class="day">23</span></div>
      <div class="month__column"><span class="weekday">Sex</span><span class="day">3</span><span class="day">10</span><span class="day">17</span><span class="day">24</span></div>
      <div class="month__column month__column--tinted"><span class="weekday">Sáb</span><span class="day">4</span><span class="day">11</span><span class="day">18</span><span class="day">25</span></div>
    </div>
  </section>
</main>
</body>
</html>
```